Brochure Design Project for Family and Cosmetic Dental Practice

Family and Cosmetic Dental Practice with Ocean/Tropical Theme
Here is some more information about my business. We also have a website :www.marlowcrestsmiles.com. That has a video that we made and gives you a some more information about us.

An Overview / Background of the Business & Services :

Family and Cosmetic Dental Practice

Procedures that we do:

Clearmora (Clear Braces)

Dentures and Partials

Whitening/ Teeth Bleaching (both Brite and Vel)

Cosmetic Dentistry (veneers and esthetic crowns)

Implants

Children's Dentistry

Sedation Dentistry and Nitrous Oxide Gas (Laughing Gas)

The Target Market / Audience you are trying to reach:

Families (30 to 40 yrs with children) - Caucasians and Hispanics
People seeking cosmetic dentistry
Older Patients (50yrs +)

Design Specifics; any preferences or ideas for Style, Colour, Imagery, etc :

Color: Blues

Theme: Ocean/ Tropical

Our Philosophy

Our belief is that the best oral care that you receive is at home where you are able to maintain your oral hygiene through proper brushing, flossing and control of your diet. We would like to see you maintain your natural teeth for the rest of your life. When this is not possible we will work with you to replace them with the best aesthetic and functional restorative dentistry
that is available.

We want to let people we have been at our location for 10 years and we are family owned and are here for the long run. We are active in the community

Bios of the doctors: ( I already sent the headshot photos)

Dr Leonard Whitcombe
“Dr. Lenny”

Dr. Lenny Whitcombe attended Pemberton University for his undergraduate studies and earned a Bachelor’s degree in Chemistry. While attending Pemberton he pursued his passion of running and was a member of two Prairie Athletic League Champion cross country teams. His passion for running evolved into a desire to compete in triathlons. He continued his interest in the sciences and working with his hands by attending the Ashgrove State University College of Dentistry where he met his wife, Clara Whitcombe D.D.S. and earned his D.D.S. with honors in Oral Surgery. He has practiced the last few years in Tucson treating a wide range of patients. His desire to practice dentistry revolves around the patient and service. Some of his hobby highlights include finishing the Desert Ridge Endurance triathlon in 11 hours and 37 minutes in 2005 and a single digit golf handicap. His current passion is mountain biking. He recently finished the Ridgecrest Trail Cycling race (100 miles in one day)! Lately he spends a lot of time caring for and playing with his 3 daughters. Dr. Lenny Whitcombe is also a member of NOA (National Oral Alliance), StOC (State Oral Care Society) and GPF (Guild of Practice Fellows).

Dr. Clara Whitcombe
“Dr. Whitcombe”

Dr. Clara Whitcombe attended both Halvern College and Eastbrook Wesleyan College for her undergraduate degrees. She received a Bachelor of Science in Biology and a Bachelor of Arts in Psychology. After college, Dr Whitcombe worked for several years in the dental field while continuing her education by working towards a Master’s degree in Cell and Molecular Biology. At this point in her life Dr. Whitcombe knew that she enjoyed the dental field and decided to attend dental school. Dr. Whitcombe completed her Doctorate of Dental Surgery (D.D.S.) at Ashgrove State University where she met her husband, Dr. Leonard Whitcombe. They then moved to Tucson, Arizona in order to be close to family. When Dr. Clara isn't in the office creating beautiful smiles, she is busy with her 3 daughters and their numerous activities. Dr. Clara Whitcombe has additional training in the areas of endodontics and oral sedation. She is also a member of The National Guild of Practice Fellows (NGPF), National Oral Alliance (NOA), and State Oral Care Society (StOC). In her time outside of the office, Dr. Whitcombe enjoys traveling, spending time with her family, working out and being involved with book club.
Let me know if you need anything else!

Target Market(s)

See above

Industry/Entity Type

Business

Colors
33a6d7
85cae6
33b8a4

Requirements
Must have
• Testimonials taken from Rateway reviews. In any images used, the people must have nice smiles and teeth.

```html
<!DOCTYPE html>
<html lang="en">
<head>
<meta charset="utf-8">
<title>Marlowcrest Family Dentistry Brochure</title>
<link href="https://fonts.googleapis.com/css2?family=Open+Sans:wght@300;400;600;700&family=Lato:wght@300;400;700&display=swap" rel="stylesheet">
<style>
:root{
  --blue:#33a6d7;
  --sky:#85cae6;
  --teal:#33b8a4;
  --navy:#1d5f86;
  --deep:#1673a8;
  --ink:#4a5a66;
  --paper:#ffffff;
  --mist:#eaf6fc;
}
*{box-sizing:border-box;margin:0;padding:0}
html,body{width:867px;height:1200px;overflow:hidden;background:#dfe6ea}
body{position:relative;font-family:"Open Sans",sans-serif;color:var(--ink)}
.sheet{position:absolute;left:0;width:867px;overflow:hidden}
.outside{top:0;height:590px;background:linear-gradient(180deg,#d7eef9 0%,#ffffff 38%,#bfe3f4 62%,#4aaede 100%)}
.inside{top:616px;height:584px;background:var(--paper)}
.photo{position:absolute}
.abs{position:absolute}
.fold{position:absolute;top:0;bottom:0;width:1px;background:rgba(255,255,255,.5)}

/* outside: left panel */
.team-photo{left:14px;top:14px;width:262px;height:262px;border-radius:12px;background:linear-gradient(160deg,#b9d6e6,#5d7f99 60%,#2f4a60)}
.welcome{left:0;top:286px;width:289px;height:304px;background:linear-gradient(180deg,#3fa8dc,#1d7fba);padding:14px 18px;color:#fff;font-size:8.4px;line-height:1.5}
.welcome p{margin-bottom:7px}

/* outside: middle panel */
.contact-intro{left:300px;top:26px;width:266px;text-align:center;font-size:11px;line-height:1.45;color:var(--navy)}
.map{left:334px;top:78px;width:200px;height:200px;border-radius:50%;background:linear-gradient(135deg,#f1efe6,#e3ecd8);border:5px solid #fff;box-shadow:0 0 10px rgba(0,0,0,.15)}
.address{left:300px;top:292px;width:266px;text-align:center;font-size:10px;line-height:1.55;color:var(--navy)}
.address .site{color:var(--deep);font-weight:600}

/* outside: right panel */
.brand{left:606px;top:26px;display:flex;align-items:center;gap:8px}
.brand .mark{width:30px;height:30px;background:var(--navy)}
.brand .name{font-family:"Lato",sans-serif;font-weight:700;font-size:17px;line-height:1.05;color:var(--navy);text-transform:uppercase;letter-spacing:.5px}
.family-photo{left:578px;top:84px;width:289px;height:250px;background:radial-gradient(ellipse at 50% 50%,#f1d9c4 0%,#d8e9f3 55%,rgba(215,238,249,0) 75%)}
.tagline{left:590px;top:372px;width:266px;text-align:right;color:#fff}
.tagline .big{font-family:"Lato",sans-serif;font-weight:300;font-size:46px;line-height:1}
.tagline .rest{font-family:"Lato",sans-serif;font-weight:300;font-size:21px;line-height:1.2}
.tagline .site{margin-top:8px;font-size:12px}

/* inside */
.wave-top{left:0;top:0;width:867px;height:110px}
.section-title{font-family:"Lato",sans-serif;font-weight:300;letter-spacing:1px;text-transform:uppercase}
.doctors-title{left:0;top:18px;width:867px;text-align:center;font-size:26px;color:var(--navy)}
.tools-photo{left:12px;top:84px;width:264px;height:175px;border-radius:6px;background:linear-gradient(135deg,#e7eef2,#9fb3c0 55%,#d5dfe5)}
.procedures-title{left:18px;top:278px;font-size:27px;color:var(--navy)}
.procedures{left:18px;top:318px;width:252px;font-size:8.6px;line-height:1.55;color:var(--ink)}
.procedures p{margin-bottom:8px}
.doc-circle{border-radius:50%;border:4px solid #fff;box-shadow:0 0 8px rgba(0,0,0,.18);background:radial-gradient(circle at 50% 40%,#e8c8ae,#8aa3b4 70%)}
.doc1-photo{left:470px;top:70px;width:100px;height:100px}
.doc2-photo{left:296px;top:276px;width:100px;height:100px}
.doc-name{font-family:"Lato",sans-serif;font-weight:700;font-size:11px;color:var(--deep)}
.doc-bio{font-size:7.6px;line-height:1.5;color:var(--ink)}
.doc1-name{left:300px;top:84px}
.doc1-bio{left:300px;top:102px;width:164px}
.doc1-bio2{left:300px;top:184px;width:272px}
.doc2-name{left:404px;top:286px}
.doc2-bio{left:404px;top:304px;width:168px}
.doc2-bio2{left:300px;top:386px;width:272px}
.patient-photo{left:660px;top:60px;width:207px;height:200px;background:linear-gradient(135deg,#d2e9f5,#e9cdb7 55%,#8bbad3)}
.patient-circle{left:600px;top:150px;width:86px;height:86px}
.testimonials-title{left:600px;top:278px;font-size:27px;color:var(--navy)}
.quotes{left:600px;top:318px;width:252px;font-size:8.6px;line-height:1.55;color:var(--ink)}
.quotes p{margin-bottom:10px}
.quotes .by{display:block;text-align:right;font-style:italic;color:var(--deep)}
.wave-bottom{left:0;bottom:0;width:867px;height:60px}
</style>
</head>
<body>

<section class="sheet outside">
  <div class="fold" style="left:289px"></div>
  <div class="fold" style="left:578px"></div>

  <div class="photo team-photo" role="img" aria-label="Photo of the two dentists standing together in the office"></div>
  <div class="abs welcome">
    <p>Welcome to Marlowcrest Family Dentistry. We are a family owned practice and have proudly served our neighbors at this location for ten years, and we are here for the long run.</p>
    <p>Our belief is that the best oral care happens at home through proper brushing, flossing and a balanced diet. We want to help you keep your natural teeth for the rest of your life, and when that is not possible we will restore them with the finest aesthetic and functional dentistry available.</p>
    <p>Dr. Leonard Whitcombe and Dr. Clara Whitcombe have additional training in sedation and endodontics, so every member of your family can feel relaxed in our care. We are active in our community and look forward to meeting you.</p>
  </div>

  <p class="abs contact-intro">We encourage you to contact<br>us with any questions or<br>comments you may have</p>
  <div class="photo map" role="img" aria-label="Street map showing the practice location"></div>
  <div class="abs address">
    2150 Harbor Crest Drive<br>
    Suite 116 Bayview, AZ 85000<br>
    (480) 555-0142<br>
    <span class="site">www.marlowcrestsmiles.com</span>
  </div>

  <div class="abs brand">
    <span class="mark"></span>
    <span class="name">Marlowcrest<br>Family Dentistry</span>
  </div>
  <div class="photo family-photo" role="img" aria-label="Photo of a smiling family with two children"></div>
  <div class="abs tagline">
    <div class="big">Quality</div>
    <div class="rest">Dentistry With a<br>Compassionate Touch</div>
    <div class="site">www.marlowcrestsmiles.com</div>
  </div>
</section>

<section class="sheet inside">
  <svg class="abs wave-top" viewBox="0 0 867 110" preserveAspectRatio="none" aria-hidden="true">
    <path d="M0 0H867V48C700 78 560 40 430 62 300 84 150 50 0 70Z" fill="#85cae6" opacity=".55"/>
    <path d="M0 0H867V30C700 58 560 22 430 44 300 66 150 32 0 50Z" fill="#33a6d7" opacity=".35"/>
  </svg>
  <h2 class="abs section-title doctors-title">Our Doctors</h2>

  <div class="photo tools-photo" role="img" aria-label="Photo of dental instruments on a tray"></div>
  <h2 class="abs section-title procedures-title">Procedures</h2>
  <div class="abs procedures">
    <p>Whether your dental needs are a complete exam and cleaning, a full mouth restoration, or anything in between, we promise to provide you with exceptional care as we enhance the natural beauty of your smile. Below are some of the many procedures and services we regularly provide to our patients, with a gentle touch and stunning results. Your smile is our first priority and we'll give you something to smile about.</p>
    <p>If you have any questions, concerns, or would like to schedule an appointment, please contact us. We look forward to providing you with the personal care you deserve.</p>
    <p>Sincerely,<br>Dr. Leonard Whitcombe<br>Dr. Clara Whitcombe</p>
  </div>

  <div class="photo doc-circle doc1-photo" role="img" aria-label="Headshot of Dr. Leonard Whitcombe"></div>
  <div class="abs doc-name doc1-name">Dr Leonard Whitcombe</div>
  <p class="abs doc-bio doc1-bio">Dr. Lenny Whitcombe attended Pemberton University and earned a Bachelor's degree in Chemistry, running on two Prairie Athletic League Champion cross country teams.</p>
  <p class="abs doc-bio doc1-bio2">He attended the Ashgrove State University College of Dentistry, where he met his wife and earned his D.D.S. with honors in Oral Surgery. He finished the Desert Ridge Endurance triathlon and the Ridgecrest Trail Cycling race, and now spends his time with his 3 daughters. He is a member of the NOA, StOC and GPF.</p>

  <div class="photo doc-circle doc2-photo" role="img" aria-label="Headshot of Dr. Clara Whitcombe"></div>
  <div class="abs doc-name doc2-name">Dr. Clara Whitcombe</div>
  <p class="abs doc-bio doc2-bio">Dr. Clara Whitcombe attended Halvern College and Eastbrook Wesleyan College, earning degrees in Biology and Psychology.</p>
  <p class="abs doc-bio doc2-bio2">She completed her Doctorate of Dental Surgery at Ashgrove State University, where she met her husband, Dr. Leonard Whitcombe. She has additional training in endodontics and oral sedation and is a member of the NGPF, NOA and StOC. Outside the office she enjoys travel, her family and book club.</p>

  <div class="photo patient-photo" role="img" aria-label="Photo of a smiling man with a bright smile"></div>
  <div class="photo doc-circle patient-circle" role="img" aria-label="Photo of a smiling woman"></div>
  <h2 class="abs section-title testimonials-title">Testimonials</h2>
  <div class="abs quotes">
    <p>"Both doctors have been wonderful. The staff is friendly and made my whole family feel right at home. My kids actually look forward to their visits now and ask when they can go back!" <span class="by">— Rateway review</span></p>
    <p>"Honest, gentle and thorough care every single time. I was nervous about my crowns but the results look completely natural. I would recommend this practice to anyone who wants a beautiful smile." <span class="by">— Rateway review</span></p>
  </div>

  <svg class="abs wave-bottom" viewBox="0 0 867 60" preserveAspectRatio="none" aria-hidden="true">
    <path d="M0 30C160 10 300 50 450 30 600 10 740 42 867 24V60H0Z" fill="#85cae6" opacity=".5"/>
    <path d="M0 44C160 28 320 60 470 44 620 28 760 54 867 40V60H0Z" fill="#33a6d7" opacity=".55"/>
  </svg>
</section>

</body>
</html>
```